Bref créative
Quorel Stationary
Stationary and Business Cards
I need double sided standard sized Business Card [3.5" x 2"]
show me your ideas
Corporate
Marcus Toddin
Chief Executive Officer
Halvenor Business Tower
18th Floor
PO Box 58217
Dubai
United Arab Emirates
mt@quorel.co
www.quorel.co
Show me your ideas

```html
<!DOCTYPE html>
<html lang="en">
<head>
<meta charset="utf-8">
<title>Quorel Stationary – Stationery Set</title>
<link href="https://fonts.googleapis.com/css2?family=Cinzel:wght@400;600&family=Arimo:wght@400;700&display=swap" rel="stylesheet">
<style>
  :root{
    --backdrop:#e9e6e1;
    --paper:#ffffff;
    --edge:#d6d3ce;
    --brand:#2a9fd8;
    --brand-dark:#1683c2;
    --brand-light:#63c6f2;
    --ink:#4a4a4a;
    --ink-soft:#7a7a7a;
    --label:#ffffff;
    --label-bg:#8b857d;
  }
  *{box-sizing:border-box;margin:0;padding:0}
  html,body{width:1200px;height:932px;overflow:hidden}
  body{background:var(--backdrop);position:relative;font-family:"Cinzel",serif;color:var(--ink)}
  .sheet{position:absolute;background:var(--paper);border:1px solid var(--edge);box-shadow:0 2px 6px rgba(0,0,0,.12)}
  .label{position:absolute;font-family:"Arimo",sans-serif;font-weight:700;font-size:12px;letter-spacing:.08em;color:var(--label);background:var(--label-bg);padding:2px 6px}

  .brand{display:flex;align-items:center;gap:8px}
  .brand-dot{border-radius:50%;background:var(--brand)}
  .brand-name{font-family:"Cinzel",serif;font-weight:600;color:var(--brand)}

  /* Fax */
  .fax{left:38px;top:157px;width:568px;height:740px}
  .fax .brand{position:absolute;left:36px;top:38px}
  .fax-title{position:absolute;left:28px;top:112px;font-family:"Arimo",sans-serif;font-size:46px;color:#222}
  .fax-fields{position:absolute;left:28px;top:200px;width:520px;list-style:none}
  .fax-fields li{font-family:"Arimo",sans-serif;font-size:14px;color:#333;height:42px;display:flex;align-items:flex-end;padding-bottom:4px}
  .fax-fields li span{flex:1;border-bottom:1px solid #999;margin-left:6px;height:1px}
  .fax-checks{position:absolute;left:28px;top:410px;display:flex;gap:36px;font-family:"Arimo",sans-serif;font-size:13px;color:#333}
  .fax-checks span::before{content:"";display:inline-block;width:12px;height:12px;border:1px solid #888;background:#eee;margin-right:7px;vertical-align:-2px}

  /* Letterhead */
  .letterhead{left:222px;top:38px;width:612px;height:581px}
  .lh-head{position:absolute;left:30px;top:26px;display:flex;align-items:flex-start;gap:18px}
  .divider{width:1px;background:#bbb;align-self:stretch}
  .contact{font-size:11px;line-height:1.45;color:var(--ink)}
  .contact .line{display:flex;align-items:center;gap:6px}
  .icon{width:10px;height:10px;flex:none}

  /* Envelope */
  .envelope{left:505px;top:290px;width:392px;height:329px}
  .env-flap{position:absolute;left:0;top:0}
  .env-top{position:absolute;left:174px;top:14px}
  .env-brand{position:absolute;left:22px;top:160px}
  .env-web{position:absolute;left:22px;top:236px;font-size:15px;color:var(--brand)}
  .env-addr{position:absolute;left:22px;top:260px;font-size:11px;line-height:1.5}

  /* Business cards */
  .card{width:273px;height:114px}
  .card-front{display:flex;align-items:center;padding:0 14px;gap:12px}
  .card-front .contact{font-size:7.5px;line-height:1.4}
  .card-name{font-size:10.5px;color:var(--brand);font-weight:600}
  .card-title{font-size:7px;color:var(--ink-soft);margin-bottom:5px}
  .card-a{left:859px;top:63px}
  .card-c{left:758px;top:783px;width:417px;height:114px}
  .card-c .contact{font-size:9px}
  .card-c .card-name{font-size:13px}
  .card-back{left:909px;top:606px;width:266px;height:126px;background:linear-gradient(135deg,var(--brand-dark),var(--brand-light));border:none;display:flex;flex-direction:column;align-items:center;justify-content:center;gap:6px}
  .card-back .brand-name{color:#fff}
  .card-back .brand-dot{background:#fff}
  .card-back .web{font-size:8px;color:#eaf7ff}

  .vertical{position:absolute;left:1163px;top:330px;writing-mode:vertical-rl;font-family:"Arimo",sans-serif;font-weight:700;font-size:12px;letter-spacing:.08em;color:var(--label);background:var(--label-bg);padding:6px 2px}
</style>
</head>
<body>

<span class="label" style="left:24px;top:132px">FAX</span>
<span class="label" style="left:485px;top:12px">LETTERHEAD</span>
<span class="label" style="left:900px;top:36px">BUSINESS CARD - FRONT</span>
<span class="label" style="left:945px;top:748px">BUSINESS CARD - BACK</span>
<span class="vertical">ENVELOPE</span>

<!-- Fax -->
<section class="sheet fax">
  <div class="brand"><span class="brand-dot" style="width:26px;height:26px"></span><span class="brand-name" style="font-size:24px">Quorel</span></div>
  <h1 class="fax-title">FAX</h1>
  <ul class="fax-fields">
    <li>To :<span></span></li>
    <li>Fax :<span></span></li>
    <li>Phone :<span></span></li>
    <li>Re :<span></span></li>
  </ul>
  <div class="fax-checks"><span>Urgent</span><span>For Review</span></div>
</section>

<!-- Letterhead -->
<section class="sheet letterhead">
  <div class="lh-head">
    <div class="brand"><span class="brand-dot" style="width:28px;height:28px"></span><span class="brand-name" style="font-size:26px">Quorel</span></div>
    <span class="divider"></span>
    <div class="contact">
      <div>Halvenor Business Tower,</div>
      <div>18th Floor, PO Box 58217</div>
      <div>Dubai, United Arab Emirates</div>
      <div class="line" style="margin-top:4px"><svg class="icon" viewBox="0 0 10 10"><rect x="0.5" y="1.5" width="9" height="7" fill="none" stroke="#2a9fd8"/><path d="M0.5 1.5 5 5.5 9.5 1.5" fill="none" stroke="#2a9fd8"/></svg>mt@quorel.co</div>
      <div class="line"><svg class="icon" viewBox="0 0 10 10"><circle cx="5" cy="5" r="4.3" fill="none" stroke="#2a9fd8"/><path d="M0.7 5h8.6M5 0.7c-2.4 2.6-2.4 6 0 8.6M5 0.7c2.4 2.6 2.4 6 0 8.6" fill="none" stroke="#2a9fd8" stroke-width=".8"/></svg>www.quorel.co</div>
    </div>
  </div>
</section>

<!-- Envelope -->
<section class="sheet envelope">
  <svg class="env-flap" width="392" height="140" viewBox="0 0 392 140"><path d="M0 0 L196 110 L392 0" fill="none" stroke="#e2e0dc" stroke-width="1.5"/></svg>
  <div class="brand env-top"><span class="brand-dot" style="width:12px;height:12px"></span><span class="brand-name" style="font-size:11px">Quorel</span></div>
  <div class="brand env-brand"><span class="brand-dot" style="width:40px;height:40px"></span><span class="brand-name" style="font-size:30px">Quorel</span></div>
  <div class="env-web">www.quorel.co</div>
  <div class="env-addr">
    <div>Halvenor Business Tower, 18th Floor,</div>
    <div>PO Box 58217, Dubai, United Arab Emirates</div>
  </div>
</section>

<!-- Business card front -->
<section class="sheet card card-front card-a">
  <div class="brand"><span class="brand-dot" style="width:16px;height:16px"></span><span class="brand-name" style="font-size:15px">Quorel</span></div>
  <span class="divider"></span>
  <div class="contact">
    <div class="card-name">Marcus Toddin</div>
    <div class="card-title">Chief Executive Officer</div>
    <div>Halvenor Business Tower, 18th Floor</div>
    <div>PO Box 58217, Dubai, UAE</div>
    <div>mt@quorel.co</div>
    <div>www.quorel.co</div>
  </div>
</section>

<!-- Business card back -->
<section class="sheet card card-back">
  <div class="brand"><span class="brand-dot" style="width:22px;height:22px"></span><span class="brand-name" style="font-size:22px">Quorel</span></div>
  <div class="web">www.quorel.co</div>
</section>

<!-- Business card front, larger -->
<section class="sheet card card-front card-c">
  <div class="brand"><span class="brand-dot" style="width:22px;height:22px"></span><span class="brand-name" style="font-size:22px">Quorel</span></div>
  <span class="divider"></span>
  <div class="contact">
    <div class="card-name">Marcus Toddin</div>
    <div class="card-title" style="font-size:9px">Chief Executive Officer</div>
    <div>Halvenor Business Tower, 18th Floor</div>
    <div>PO Box 58217, Dubai, United Arab Emirates</div>
    <div>mt@quorel.co</div>
    <div>www.quorel.co</div>
  </div>
</section>

</body>
</html>
```